Stationary Design for Stunning new Logo

I need to envelopes, letterhead, business cards designed to compliment our new logo.

We are a 25 year old printing company going through a brand refresh. All items should have the design extended to both sides for full print ability.

Industry/Entity Type

Printing

Requirements
Must have
• It must utilize the new logo & colors PMS 300 & PMS 295.

```html
<!DOCTYPE html>
<html lang="en">
<head>
<meta charset="utf-8">
<title>NORTHPRESS Stationery Set</title>
<link href="https://fonts.googleapis.com/css2?family=Open+Sans:ital,wght@0,400;0,700;0,800;1,400&display=swap" rel="stylesheet">
<style>
  :root {
    --navy: #1d355e;
    --blue: #0f62ac;
    --paper: #ffffff;
    --ink: #333333;
    --backdrop: #e8e5e1;
    --edge: #d4d0cb;
    --flap: #f6f5f3;
    --rule: #9aa3ad;
  }
  * { margin: 0; padding: 0; box-sizing: border-box; }
  html, body { width: 1200px; height: 811px; overflow: hidden; }
  body {
    position: relative;
    background: var(--backdrop);
    font-family: "Open Sans", Arial, sans-serif;
    color: var(--ink);
  }
  .sheet {
    position: absolute;
    background: var(--paper);
    box-shadow: 0 1px 3px rgba(0,0,0,.18);
    overflow: hidden;
  }

  /* brand lockup: name plus one plain circle */
  .brand {
    position: absolute;
    display: flex;
    align-items: center;
    gap: .3em;
    font-size: var(--s);
    white-space: nowrap;
  }
  .brand-mark { width: 1em; height: 1em; border-radius: 50%; background: var(--navy); flex: none; }
  .brand-name { font-weight: 800; color: var(--navy); line-height: 1; letter-spacing: -.01em; }

  /* corner bands */
  .band { position: absolute; }
  .band-dark { background: var(--navy); }
  .band-light { background: var(--blue); }

  /* letterhead */
  .letterhead-front { left: 263px; top: 78px; width: 317px; height: 449px; }
  .letterhead-back  { left: 600px; top: 62px; width: 340px; height: 483px; }
  .letter-body {
    position: absolute; left: 24px; top: 96px; width: 276px;
    font-size: 5.6px; line-height: 7.4px; color: var(--ink);
  }
  .letter-body p { margin-bottom: 7.4px; }
  .letter-body .gap { margin-top: 14px; }

  /* business cards */
  .card-front { left: 88px; top: 433px; width: 127px; height: 76px; }
  .card-back  { left: 88px; top: 541px; width: 127px; height: 76px; }
  .card-name { position: absolute; left: 10px; top: 33px; font-size: 5px; font-weight: 700; color: var(--ink); line-height: 6px; }
  .card-position { display: block; font-weight: 400; font-style: italic; font-size: 4px; }
  .card-contacts { position: absolute; left: 10px; top: 47px; width: 110px; font-size: 3.6px; line-height: 5px; }
  .contact-row { display: flex; align-items: center; gap: 2px; }
  .contact-line { display: inline-block; height: 1.2px; background: var(--rule); }
  .contact-cols { display: flex; justify-content: space-between; }

  /* envelopes */
  .envelope-front { left: 263px; top: 590px; width: 338px; height: 162px; }
  .envelope-back  { left: 628px; top: 590px; width: 337px; height: 162px; }
  .envelope-flap { position: absolute; left: 0; top: 0; }
</style>
</head>
<body>

  <!-- letterhead, printed side -->
  <section class="sheet letterhead-front" aria-label="Letterhead">
    <div class="brand" style="--s:18px; left:17px; top:26px;">
      <span class="brand-mark"></span>
      <span class="brand-name">NORTHPRESS</span>
    </div>
    <div class="letter-body">
      <p>2450, Harbor View Avenue<br>Oakland, CA 94607.</p>
      <p>January 29th, 2011</p>
      <p>Mr. Calloway<br>President, Calloway Community Center<br>718 Maple Court<br>Boston, MA 02118</p>
      <p>Dear Mr. Calloway:</p>
      <p>In the first paragraph, one needs to give a brief introduction of oneself. One should also give reference to the purpose of the letter in brief.<br>The second paragraph needs to give the details of the letter and its need. This paragraph is mostly longer than the others and plays the main role in the letter. Keep the sentences short and to the point. Avoid using complex words and sentences.</p>
      <p class="gap">The third and last paragraph is the conclusion of the letter and can be kept short.</p>
      <p>Sincerely,</p>
      <p>(this is where the signature of the writer will be placed)</p>
      <p>Dana Whitfield<br>Read more at Letter Guide: http://www.letterguide.example/articles/business-letter-format.html</p>
    </div>
    <div class="band band-dark" style="left:0; top:425px; width:217px; height:11px;"></div>
    <div class="band band-light" style="left:188px; top:433px; width:129px; height:9px;"></div>
  </section>

  <!-- letterhead, reverse side -->
  <section class="sheet letterhead-back" aria-label="Letterhead reverse">
    <div class="brand" style="--s:22px; left:22px; top:424px;">
      <span class="brand-mark"></span>
      <span class="brand-name">NORTHPRESS</span>
    </div>
    <div class="band band-dark" style="left:0; top:457px; width:233px; height:8px;"></div>
    <div class="band band-light" style="left:200px; top:464px; width:140px; height:8px;"></div>
  </section>

  <!-- business card, front -->
  <section class="sheet card-front" aria-label="Business card front">
    <div class="brand" style="--s:12px; left:9px; top:32px;">
      <span class="brand-mark"></span>
      <span class="brand-name">NORTHPRESS</span>
    </div>
  </section>

  <!-- business card, back -->
  <section class="sheet card-back" aria-label="Business card back">
    <div class="brand" style="--s:9px; left:9px; top:12px;">
      <span class="brand-mark"></span>
      <span class="brand-name">NORTHPRESS</span>
    </div>
    <div class="card-name">Your Name<span class="card-position">Position</span></div>
    <div class="card-contacts">
      <div class="contact-row">Address: <span class="contact-line" style="width:34px"></span></div>
      <div class="contact-cols">
        <div class="contact-row"><span class="contact-line" style="width:40px"></span></div>
        <div class="contact-row">Fax: <span class="contact-line" style="width:34px"></span></div>
      </div>
      <div class="contact-cols">
        <div class="contact-row">Phone: <span class="contact-line" style="width:30px"></span></div>
        <div class="contact-row">Email: <span class="contact-line" style="width:30px"></span></div>
      </div>
    </div>
  </section>

  <!-- envelope, front -->
  <section class="sheet envelope-front" aria-label="Envelope front">
    <div class="brand" style="--s:13px; left:209px; top:12px;">
      <span class="brand-mark"></span>
      <span class="brand-name">NORTHPRESS</span>
    </div>
    <div class="band band-dark" style="left:0; top:141px; width:250px; height:9px;"></div>
    <div class="band band-light" style="left:200px; top:148px; width:138px; height:9px;"></div>
  </section>

  <!-- envelope, back -->
  <section class="sheet envelope-back" aria-label="Envelope back">
    <svg class="envelope-flap" width="337" height="162" viewBox="0 0 337 162" aria-hidden="true">
      <polygon points="0,0 337,0 179,48 158,48" fill="var(--flap)" stroke="var(--edge)" stroke-width="1"/>
      <polyline points="0,1 158,49 179,49 337,1" fill="none" stroke="rgba(0,0,0,.12)" stroke-width="2"/>
    </svg>
    <div class="brand" style="--s:11px; left:130px; top:12px;">
      <span class="brand-name">NORTHPRESS</span>
    </div>
    <div class="band band-dark" style="left:0; top:141px; width:250px; height:8px;"></div>
    <div class="band band-light" style="left:200px; top:148px; width:137px; height:8px;"></div>
  </section>

</body>
</html>
```